Travel Group 'Halvard Group' needs a new business card design

Halvard Group is a diverse business specialising in bespoke, tailor made holidays to suit all budgets and we are specialists in planning exciting day/short trips to suit all markets. Our target market is very varied going from the corporate client and as well as people in the community who simply want to experience something special.
We are looking for a card design that will encourage people to look at our websites and social media platforms and to see for themselves the different facets to our business. It is essential that the card has social media icons for Pagebloom, Quibbly and Snapverse. We are looking for a card with a blank background with no pictures and for the front side to have the attached Halvard logo. The card should have similar colour scheme to the attached Halvard logo.
The card must have the following information on one side:
Maren Doyle
Business Development Manager
marendoyle@halvardtravel.example
Halvard Group, 48 Fenwick Row
Dunmarrow, Glenridge, Scotland KB27 4RT
+44 (0)1632 960418
And then the card must have the following on the second side:
(Halvard logo)
(social media icons)
www.halvardtravel.example
www.halvardexperience.example
Target Market(s)
Our target market is very varied going from the corporate client and as well as people in the community who simply want to experience something special.
Industry/Entity Type
Business
Contact Information for Business Card
Maren Doyle
+44 (0)1632 960418
(Halvard logo)
(social media icons)
www.halvardtravel.example
www.halvardexperience.example
Requirements
Must have
- It is essential that the card has social media icons for Pagebloom, Quibbly & Snapverse.
Should not have
- Should not have any images other than Halvard logo.

```html
<!DOCTYPE html>
<html lang="en">
<head>
<meta charset="utf-8">
<title>Halvard Group – Business Card</title>
<link rel="stylesheet" href="https://fonts.googleapis.com/css2?family=Libre+Baskerville:wght@400;700&family=Open+Sans:wght@400;600&display=swap">
<style>
  :root {
    --backdrop: #4a4540;
    --card: #0c0c0d;
    --card-edge: #1c1c1e;
    --magenta: #e0168f;
    --violet: #5a3bb0;
    --silver: #b9b9bd;
    --ink: #f2f2f2;
    --rule: #3a3a3d;
  }
  * { box-sizing: border-box; margin: 0; padding: 0; }
  html, body { width: 1200px; height: 900px; overflow: hidden; }
  body {
    background: var(--backdrop);
    display: flex;
    align-items: center;
    justify-content: center;
    gap: 40px;
    font-family: "Open Sans", Arial, sans-serif;
  }
  .card {
    width: 540px;
    height: 318px;
    background: var(--card);
    border: 1px solid var(--card-edge);
    box-shadow: 0 10px 30px rgba(0,0,0,.45);
    position: relative;
  }

  /* Contact side */
  .card--contact { display: flex; }
  .brand-panel {
    width: 48%;
    display: flex;
    align-items: center;
    justify-content: center;
    gap: 12px;
    border-right: 1px solid var(--rule);
    margin: 28px 0;
  }
  .brand-mark {
    width: 26px; height: 26px;
    border-radius: 50%;
    background: var(--magenta);
  }
  .brand-name {
    font-family: "Libre Baskerville", Georgia, serif;
    font-weight: 700;
    font-size: 28px;
    letter-spacing: 2px;
    color: var(--violet);
  }
  .contact-panel {
    flex: 1;
    padding: 48px 20px 0 22px;
    color: var(--ink);
  }
  .person-name {
    font-family: "Libre Baskerville", Georgia, serif;
    font-weight: 700;
    font-size: 17px;
    color: var(--magenta);
    letter-spacing: .5px;
  }
  .person-role { font-size: 12.5px; margin: 2px 0 12px; }
  .contact-list { list-style: none; font-size: 12px; line-height: 1.55; }
  .contact-list li { display: flex; align-items: flex-start; gap: 8px; }
  .contact-icon { width: 11px; height: 11px; margin-top: 4px; flex: none; fill: var(--magenta); }
  .address { margin-top: 6px; font-size: 12.5px; line-height: 1.45; padding-left: 19px; }

  /* Brand side */
  .card--brand {
    display: flex;
    flex-direction: column;
    align-items: center;
    justify-content: center;
  }
  .brand-lockup { display: flex; align-items: center; gap: 14px; }
  .brand-lockup .brand-mark { background: var(--silver); width: 30px; height: 30px; }
  .brand-lockup .brand-name { color: var(--silver); font-size: 34px; }
  .social-row {
    display: flex;
    align-items: center;
    gap: 8px;
    margin-top: 26px;
  }
  .social-rule { width: 60px; height: 1px; background: var(--silver); }
  .social-icon { width: 18px; height: 18px; background: var(--ink); }
</style>
</head>
<body>

  <section class="card card--contact">
    <div class="brand-panel">
      <span class="brand-mark"></span>
      <span class="brand-name">HALVARD</span>
    </div>
    <div class="contact-panel">
      <h1 class="person-name">MAREN DOYLE</h1>
      <p class="person-role">Business Development Manager</p>
      <ul class="contact-list">
        <li>
          <svg class="contact-icon" viewBox="0 0 12 12"><path d="M2 1h3l1 3-1.5 1a6 6 0 0 0 2.5 2.5L8 6l3 1v3a1 1 0 0 1-1 1A9 9 0 0 1 1 2a1 1 0 0 1 1-1z"/></svg>
          +44 (0)1632 960418
        </li>
        <li>
          <svg class="contact-icon" viewBox="0 0 12 12"><path d="M0 2h12v8H0z M0 2l6 4 6-4" stroke="#0c0c0d" stroke-width=".8"/></svg>
          marendoyle@halvardtravel.example
        </li>
        <li>
          <svg class="contact-icon" viewBox="0 0 12 12"><circle cx="6" cy="6" r="6"/><path d="M0 6h12M6 0c-3 3-3 9 0 12M6 0c3 3 3 9 0 12" stroke="#0c0c0d" stroke-width=".8" fill="none"/></svg>
          www.halvardtravel.example
        </li>
        <li>
          <svg class="contact-icon" viewBox="0 0 12 12"><circle cx="6" cy="6" r="6"/><path d="M0 6h12M6 0c-3 3-3 9 0 12M6 0c3 3 3 9 0 12" stroke="#0c0c0d" stroke-width=".8" fill="none"/></svg>
          www.halvardexperience.example
        </li>
        <li>
          <svg class="contact-icon" viewBox="0 0 12 12"><path d="M6 0a4 4 0 0 1 4 4c0 3-4 8-4 8S2 7 2 4a4 4 0 0 1 4-4z"/><circle cx="6" cy="4" r="1.4" fill="#0c0c0d"/></svg>
          Halvard Group, 48 Fenwick Row
        </li>
      </ul>
      <p class="address">Dunmarrow, Glenridge,<br>Scotland KB27 4RT</p>
    </div>
  </section>

  <section class="card card--brand">
    <div class="brand-lockup">
      <span class="brand-mark"></span>
      <span class="brand-name">HALVARD</span>
    </div>
    <div class="social-row">
      <span class="social-rule"></span>
      <span class="social-icon" role="img" aria-label="Pagebloom"></span>
      <span class="social-icon" role="img" aria-label="Quibbly"></span>
      <span class="social-icon" role="img" aria-label="Snapverse"></span>
      <span class="social-rule"></span>
    </div>
  </section>

</body>
</html>
```